RWP Tax Services
RWP Tax Services -
Creative Brief
Professional
Dan Feltwicke
President
2847 Harbor Street, Suite 210 San Jose, CA 95128
dan@rwptaxdemo.com
www.rwptaxdemo.com
We want the card to look and feel like it is a combination of real estate business card and CPA business card. Tax professional (CPA office) with photo (real estate business) of president.

```html
<!DOCTYPE html>
<html lang="en">
<head>
<meta charset="utf-8">
<title>RWP Tax Services – Business Card</title>
<link rel="stylesheet" href="https://fonts.googleapis.com/css2?family=Arimo:wght@400&display=swap">
<style>
  :root {
    --page-bg: #ffffff;
    --card-green: #5a9a1c;
    --card-deep: #1f3a08;
    --card-black: #050505;
    --lime-light: #a6d444;
    --lime-mid: #7cb82a;
    --lime-dark: #3f7a10;
    --photo-tan: #c49a58;
    --photo-tan-edge: #a97f3f;
    --photo-ink: #1a1a1a;
    --text-light: #ffffff;
  }
  * { margin: 0; padding: 0; box-sizing: border-box; }
  html, body {
    width: 1200px;
    height: 991px;
    overflow: hidden;
    background: var(--page-bg);
  }
  .canvas {
    position: relative;
    width: 1200px;
    height: 991px;
  }
  .business-card {
    position: absolute;
    left: 236px;
    top: 236px;
    width: 693px;
    height: 424px;
    border-radius: 20px;
    overflow: hidden;
    font-family: "Arimo", Arial, sans-serif;
    color: var(--text-light);
  }
  .card-backdrop {
    position: absolute;
    inset: 0;
    width: 100%;
    height: 100%;
  }
  .president-photo {
    position: absolute;
    left: 78px;
    top: 75px;
    width: 161px;
    height: 143px;
    background: linear-gradient(160deg, #cfa865, var(--photo-tan) 60%, #b88c4c);
    border: 2px solid var(--photo-tan-edge);
    display: flex;
    align-items: center;
    justify-content: center;
    text-align: center;
    padding: 0 12px;
    font-size: 24px;
    line-height: 30px;
    color: var(--photo-ink);
  }
  .person {
    position: absolute;
    left: 353px;
    top: 132px;
    width: 310px;
    text-align: center;
  }
  .person-name {
    font-size: 40px;
    line-height: 44px;
    font-weight: 400;
    white-space: nowrap;
  }
  .person-title {
    font-size: 23px;
    line-height: 28px;
  }
  .address {
    position: absolute;
    right: 330px;
    top: 258px;
    text-align: right;
    font-size: 21px;
    line-height: 26px;
    font-style: normal;
    white-space: nowrap;
  }
  .contact-list {
    position: absolute;
    left: 403px;
    top: 258px;
    font-size: 21px;
    line-height: 26.5px;
    list-style: none;
    white-space: nowrap;
  }
  .contact-label {
    display: inline-block;
    width: 113px;
  }
  .contact-label.inline { width: auto; margin-right: 10px; }
</style>
</head>
<body>
<main class="canvas">
  <section class="business-card" aria-label="RWP Tax Services business card">
    <svg class="card-backdrop" viewBox="0 0 693 424" preserveAspectRatio="none" aria-hidden="true">
      <defs>
        <linearGradient id="backdropShade" x1="0" y1="1" x2="1" y2="0">
          <stop offset="0" stop-color="var(--card-green)"/>
          <stop offset="0.45" stop-color="var(--card-deep)"/>
          <stop offset="0.8" stop-color="var(--card-black)"/>
        </linearGradient>
        <radialGradient id="leftGlow" cx="0.05" cy="0.35" r="0.6">
          <stop offset="0" stop-color="#6aa824" stop-opacity="0.9"/>
          <stop offset="1" stop-color="#6aa824" stop-opacity="0"/>
        </radialGradient>
        <linearGradient id="limeWave" x1="0" y1="0" x2="0" y2="1">
          <stop offset="0" stop-color="var(--lime-light)"/>
          <stop offset="0.5" stop-color="var(--lime-mid)"/>
          <stop offset="1" stop-color="var(--lime-dark)"/>
        </linearGradient>
        <linearGradient id="swooshBand" x1="0" y1="0" x2="1" y2="0">
          <stop offset="0" stop-color="#2f5d0c" stop-opacity="0.6"/>
          <stop offset="0.7" stop-color="#0c1a04" stop-opacity="0.9"/>
          <stop offset="1" stop-color="#000000" stop-opacity="0.9"/>
        </linearGradient>
      </defs>
      <rect width="693" height="424" fill="url(#backdropShade)"/>
      <rect width="693" height="424" fill="url(#leftGlow)"/>
      <path class="wave-shadow" d="M0,262 C150,330 400,345 693,240 L693,270 C400,375 150,360 0,292 Z" fill="url(#swooshBand)"/>
      <path class="wave-lime" d="M0,290 C150,355 400,372 693,268 L693,424 L0,424 Z" fill="url(#limeWave)"/>
    </svg>

    <div class="president-photo" role="img" aria-label="Portrait photo of the president, Dan Feltwicke">RWP Tax Services</div>

    <header class="person">
      <h1 class="person-name">Dan Feltwicke</h1>
      <p class="person-title">President</p>
    </header>

    <address class="address">
      2847 Harbor Street, Suite 210<br>
      San Jose, CA 95128
    </address>

    <ul class="contact-list">
      <li><span class="contact-label">Toll free</span>(877) 555-0142</li>
      <li><span class="contact-label">Phone</span>(408) 555-0187</li>
      <li><span class="contact-label">Fax</span>(408) 555-0163</li>
      <li><span class="contact-label inline">Email</span>dan@rwptaxdemo.com</li>
      <li>www.rwptaxdemo.com</li>
    </ul>
  </section>
</main>
</body>
</html>
```